Marlow Poise & Image Consultancy

Hi, I need a brochure design for my personal styling business. I have downloaded the company logo along with the content of the services offered for the brochure. Being a colour and styling business I would been keen on having some pictures of timeless fashion or colour samples, This is not absolutely necessary just an idea. I had also thought about changing and naming the services offered with a feminine, fun interesting type of theme. This may make it more inviting, I would be really interested in any of your creative ideas in this area. I will be deciding on the business card design in the next couple of days. I will download the design for this once I have made the decision. I will be okay to pay for any photo images that may be required if the brochure is selected. I had envisaged a tri fold brochure standard letter size with two folds (8.5" by 11inchs) however I am open to any suggestions. Please feel free to make any changes or modification's to the content, font etc in the files downloaded for the brochure. Many Thanks.
Updates
Project Deadline Extended
Reason: I need to extend the time for this project as I do not have all of content required for the brochure confirmed. Many Thanks
Industry/Entity Type
Fashion
Font styles to use
Look and feel
Each slider illustrates characteristics of the customer's brand and the style your logo design should communicate.

```html
<!DOCTYPE html>
<html lang="en">
<head>
<meta charset="utf-8">
<title>Marlow Poise &amp; Image Consultancy – Brochure</title>
<link rel="stylesheet" href="https://fonts.googleapis.com/css2?family=Open+Sans:ital,wdth,wght@0,75..100,300..800;1,75..100,300..800&display=swap">
<style>
  :root{
    --charcoal:#3b3d40;
    --charcoal-deep:#2e3033;
    --paper:#e4e4e3;
    --gold:#d2b13c;
    --gold-deep:#8a6a2a;
    --ink:#3a3a3a;
    --heading-grey:#555759;
    --white:#ffffff;
    --ribbon:#dcdcdc;
  }
  *{box-sizing:border-box;margin:0;padding:0}
  html,body{width:1200px;height:847px;overflow:hidden;background:#fff}
  body{font-family:"Open Sans",Arial,sans-serif}
  .brochure{position:relative;width:1200px;height:847px;overflow:hidden;background:var(--paper)}
  .panel{position:absolute;top:0;height:847px}
  .panel--intro{left:0;width:298px;background:var(--charcoal)}
  .panel--colour{left:298px;width:298px;background:var(--paper);border-right:1px solid #c9c9c9}
  .panel--style{left:596px;width:297px;background:var(--paper)}
  .panel--makeup{left:893px;width:307px;background:var(--charcoal)}
  .artwork{position:absolute;left:0;top:0;width:1200px;height:847px}

  .copy{position:absolute;font-size:9px;line-height:11.8px;font-stretch:85%;letter-spacing:-.05px}
  .copy p{margin-bottom:3px}
  .on-dark{color:var(--white)}
  .on-light{color:var(--ink)}

  .intro-title{font-size:17px;line-height:17px;font-weight:400;font-stretch:92%;color:var(--white);text-transform:uppercase;margin-bottom:6px;white-space:nowrap}
  .services-title{color:var(--gold);font-weight:700;font-size:10.5px;line-height:13px;margin:5px 0 2px}
  .service-name{color:var(--gold);font-weight:700;text-transform:uppercase}

  .panel-heading{font-size:18px;line-height:22px;font-weight:400;font-stretch:88%;color:var(--heading-grey);letter-spacing:.2px;margin-bottom:10px;text-transform:uppercase;white-space:nowrap}
  .panel-heading--light{color:var(--white);font-size:17px}
  .session-label{font-weight:700;margin-top:4px}
  .price-bar{display:flex;align-items:center;justify-content:center;height:36px;background:var(--gold);color:var(--charcoal-deep);font-weight:700;font-size:11.5px;font-stretch:100%;margin:12px 0 6px}
  .note{font-style:italic;font-size:8.2px;line-height:11px}
  .makeup-heading{color:var(--gold);font-weight:700;font-size:10.5px;line-height:13px;text-transform:uppercase;margin:10px 0 3px}
  .duration-label{color:var(--gold);font-weight:700}
  .price-bar--makeup{margin:10px 0 5px}
  .extras{font-size:11px;line-height:14px;font-stretch:100%;margin-top:6px}

  .menu{position:absolute;left:0;top:622px;width:262px;list-style:none}
  .menu li{position:relative;height:23px;margin-bottom:5.7px;background:var(--ribbon);
    clip-path:polygon(0 0,100% 0,94% 50%,100% 100%,0 100%);
    display:flex;align-items:center;font-size:11px;color:#333;text-transform:uppercase;letter-spacing:.2px}
  .menu-number{width:56px;text-align:center;font-weight:700;font-size:14px;color:#444}
</style>
</head>
<body>
<div class="brochure">
  <div class="panel panel--intro"></div>
  <div class="panel panel--colour"></div>
  <div class="panel panel--style"></div>
  <div class="panel panel--makeup"></div>

  <svg class="artwork" viewBox="0 0 1200 847">
    <defs>
      <clipPath id="top-strip">
        <path d="M0 0 H608 C560 70 430 160 250 190 C150 205 60 200 0 192 Z"/>
      </clipPath>
      <clipPath id="bottom-strip">
        <path d="M560 847 C585 730 715 665 870 640 C1010 620 1120 618 1200 624 V847 Z"/>
      </clipPath>
      <linearGradient id="g-red" x1="0" y1="0" x2="0" y2="1"><stop offset="0" stop-color="#5a4a4a"/><stop offset="1" stop-color="#a51e24"/></linearGradient>
      <linearGradient id="g-mint" x1="0" y1="0" x2="0" y2="1"><stop offset="0" stop-color="#e7a89d"/><stop offset="1" stop-color="#c9d9d4"/></linearGradient>
      <linearGradient id="g-grey" x1="0" y1="0" x2="0" y2="1"><stop offset="0" stop-color="#b7bcbf"/><stop offset="1" stop-color="#6f716c"/></linearGradient>
      <linearGradient id="g-white" x1="0" y1="0" x2="0" y2="1"><stop offset="0" stop-color="#e9e9e9"/><stop offset="1" stop-color="#d9d6cf"/></linearGradient>
      <linearGradient id="g-bride" x1="0" y1="0" x2="0" y2="1"><stop offset="0" stop-color="#f2f2f2"/><stop offset="1" stop-color="#d6d8db"/></linearGradient>
      <linearGradient id="g-store" x1="0" y1="0" x2="1" y2="1"><stop offset="0" stop-color="#4a4347"/><stop offset="1" stop-color="#c8b7ae"/></linearGradient>
      <linearGradient id="g-shoes" x1="0" y1="0" x2="0" y2="1"><stop offset="0" stop-color="#d3c9cc"/><stop offset="1" stop-color="#efe9e6"/></linearGradient>
      <linearGradient id="g-palette" x1="0" y1="0" x2="0" y2="1"><stop offset="0" stop-color="#e9e6e3"/><stop offset="1" stop-color="#d5b9a8"/></linearGradient>
      <linearGradient id="g-face" x1="0" y1="0" x2="0" y2="1"><stop offset="0" stop-color="#3a1d1e"/><stop offset="1" stop-color="#b4887a"/></linearGradient>
      <linearGradient id="g-lips" x1="0" y1="0" x2="0" y2="1"><stop offset="0" stop-color="#f1ece9"/><stop offset="1" stop-color="#c43a3c"/></linearGradient>
    </defs>

    <g clip-path="url(#top-strip)">
      <rect x="0" y="0" width="620" height="240" fill="#4a4c4f"/>
      <rect x="0" y="0" width="165" height="240" fill="url(#g-red)" role="img" aria-label="Model in a flowing red gown"/>
      <rect x="172" y="0" width="160" height="240" fill="url(#g-mint)" role="img" aria-label="Model in a mint jacket and white trousers"/>
      <rect x="340" y="0" width="140" height="240" fill="url(#g-grey)" role="img" aria-label="Model in a patterned summer dress"/>
      <rect x="488" y="0" width="132" height="240" fill="url(#g-white)" role="img" aria-label="Model in a white evening dress"/>
    </g>
    <path d="M608 0 H628 C570 95 430 190 250 214 C150 226 60 222 0 214 V192 C60 200 150 205 250 190 C430 160 560 70 608 0 Z" fill="var(--gold)"/>
    <path d="M628 0 H640 C585 100 440 200 255 225 C150 238 60 234 0 226 V214 C60 222 150 226 250 214 C430 190 570 95 628 0 Z" fill="var(--gold-deep)"/>
    <path d="M640 0 H652 C600 105 450 208 260 236 C150 250 60 246 0 238 V226 C60 234 150 238 255 225 C440 200 585 100 640 0 Z" fill="var(--gold)"/>

    <circle cx="686" cy="98" r="97" fill="var(--white)"/>
    <circle cx="686" cy="98" r="90" fill="url(#g-bride)" role="img" aria-label="Bride in a white gown seated on a blue sofa"/>
    <circle cx="826" cy="195" r="50" fill="var(--gold)"/>
    <circle cx="826" cy="195" r="45" fill="url(#g-store)" role="img" aria-label="Woman shopping among clothing rails"/>

    <path d="M520 847 C545 705 690 630 860 606 C1000 586 1120 588 1200 592 V624 C1120 618 1010 620 870 640 C715 665 585 730 560 847 Z" fill="var(--gold)"/>
    <g clip-path="url(#bottom-strip)">
      <rect x="540" y="590" width="660" height="257" fill="var(--charcoal-deep)"/>
      <rect x="540" y="590" width="80" height="257" fill="#cfc6c6" role="img" aria-label="Boutique clothing rail"/>
      <rect x="625" y="590" width="165" height="257" fill="url(#g-shoes)" role="img" aria-label="Woman trying on shoes in a boutique"/>
      <rect x="797" y="590" width="143" height="257" fill="url(#g-palette)" role="img" aria-label="Make-up artist holding an eyeshadow palette"/>
      <rect x="955" y="590" width="125" height="257" fill="url(#g-face)" role="img" aria-label="Dramatic evening make-up look"/>
      <rect x="1087" y="590" width="113" height="257" fill="url(#g-lips)" role="img" aria-label="Red lips and manicured nails close-up"/>
    </g>
  </svg>

  <section class="copy on-dark" style="left:30px;top:258px;width:252px">
    <h1 class="intro-title">Marlow<br>Dress for the life you love</h1>
    <p>Time for a change, take a fresh look and discover how to dress in a style that reflects your personality &amp; lifestyle. Be confident, look amazing &amp; feel great about the way that you look every day. Some people always look effortlessly stylish, looking good is all about knowing what suits you.</p>
    <p>As a personal stylist I am committed to creating a fabulous style that works for you. I take time to engage with my clients, learn about your lifestyle and work through a process to establish your signature style. Be empowered and understand how you can dress for success every day. Discover the elements in creating an overall balance and harmony in putting together a stylish functional wardrobe that reflects you and your lifestyle.</p>
    <h2 class="services-title">PERSONAL STYLING SERVICES</h2>
    <p><span class="service-name">Colour Analysis</span> – you will discover your colours and how to wear them with confidence.</p>
    <p><span class="service-name">Image &amp; Style Consultation</span> – Express your image &amp; personality through the clothes that you wear and how you wear them. Learn how to select fabrics and clothing styles that will suit &amp; flatter your shape, and how to coordinate them.</p>
    <p><span class="service-name">Wardrobe Make Over</span> – Clear out and reassess your wardrobe to ensure it reflects your life style &amp; personality.</p>
    <p><span class="service-name">Style Me Complete</span> – Accessories &amp; pulling it all together, add the finishing touches to your look with the choice of shoes and accessories, your hair style &amp; make up</p>
  </section>

  <ol class="menu">
    <li><span class="menu-number">1</span>Personal Shopping</li>
    <li><span class="menu-number">2</span>Make Up Lessons</li>
    <li><span class="menu-number">3</span>Special Occasion Make Up</li>
    <li><span class="menu-number">4</span>Seasonal Review &amp; Update</li>
    <li><span class="menu-number">5</span>Party &amp; Group Experiences</li>
    <li><span class="menu-number">6</span>Complete Makeovers</li>
    <li><span class="menu-number">7</span>Personal Styling Packages</li>
  </ol>

  <section class="copy on-light" style="left:318px;top:278px;width:256px">
    <h2 class="panel-heading">Marlow Color Consultation</h2>
    <p>Discover how colour can enhance your appearance. When you wear colour that best suits you, you will appear more vibrant; your eyes will sparkle, giving you a more youthful and healthier appearance.</p>
    <p>During an individual colour consultation you will discover</p>
    <p>What your dominant colouring or season is, which colours suit you.</p>
    <p>How to select colour for garments to flatter your body shape.</p>
    <p>How to select and wear colours to suit your personality and lifestyle.</p>
    <p>How to coordinate &amp; wear colours in your wardrobe.</p>
    <p>Experience with a make-up makeover, what makeup colours and shades to select to flatter your colouring.</p>
    <p class="session-label">SESSION:</p>
    <p><b>Duration -</b> 1 hour 30mins to 2 hours</p>
    <p><b>Includes -</b> Takeaway a colour swatch of your best colours.</p>
    <p>Information workbook with personalised notes discussed during the consultation</p>
    <div class="price-bar">Cost &nbsp;&nbsp;$225.00</div>
    <h2 class="panel-heading" style="margin-top:14px;margin-bottom:6px">Marlow Personal Shopping</h2>
    <p>So much fun! Enjoy a fun and informative shopping experience. Discover how to select styles that will compliment your figure, and personality. With my expert knowledge on knowing what is going to suit you. I can save you time and have you looking fabulous for any occasion. Shop smart with me and never waste money again on buying clothes that don't look and feel great.</p>
    <div class="price-bar">Cost: $80.00</div>
  </section>

  <section class="copy on-light" style="left:615px;top:268px;width:257px">
    <h2 class="panel-heading">Marlow Style Consultation</h2>
    <p>Discover how to dress every day with confidence. Looking good is all about knowing what suits you. If you find choosing what to wear a nightmare! Or if you are not sure that what you are wearing really suits you and looks good. Or do you have a wardrobe that never seems to have anything in it that you are excited to wear. Book in for a style consultation and change your life. Learn the skills to looking fabulous, dressing in a style that works for you.</p>
    <p>Discover &amp; understand your clothing personality and how to dress in a style that reflects your image.</p>
    <p>Understand and love your body shape, learn how to dress your proportions to highlight your best features and conceal any challenges.</p>
    <p>Select fabrics that suit your personality &amp; flatter your body shape.</p>
    <p>Understand how to coordinate and pull an outfit all together</p>
    <p class="session-label">SESSION:</p>
    <p><b>DURATION:</b> 1 hour 30 - 2 hours</p>
    <div class="price-bar" style="margin-top:6px">Cost: $165.00</div>
    <p class="note">Includes: Receive a personalized workbook full of information discussed during the session.</p>
  </section>

  <section class="copy on-dark" style="left:913px;top:44px;width:257px">
    <h2 class="panel-heading panel-heading--light" style="margin-bottom:4px">Marlow Make Up Services</h2>
    <h3 class="makeup-heading" style="margin-top:6px">Special Occasion Make Up</h3>
    <p>Be Beautiful, Get celebrity treatment and look amazing for that special occasion. Having your make up professional applied using expert techniques, you can relax &amp; feel confident that you are looking your most gorgeous.</p>
    <div class="price-bar price-bar--makeup">Cost: $85.00 per person</div>
    <p class="note">Wedding packages are available on request.</p>
    <h3 class="makeup-heading">Make Up Lesson</h3>
    <p>Learn how to apply your make up like an expert, during this lesson you will discover how to enhance your features, create a flawless finish and make those eyes sparkle using the colours that flatter you. This session provides hands on process for you to learn the application techniques required to best suit you.</p>
    <p><span class="duration-label">DURATION:</span> Approx.1.30 to 2 hours</p>
    <div class="price-bar price-bar--makeup">Cost: $95.00 per person</div>
    <p class="note">Includes Makeup chart with personalized notes on session.</p>
    <h3 class="makeup-heading" style="margin-top:14px">Make Up Season Update</h3>
    <p>Have you been applying your make up the same way for years? Or do you just want to look and feel confident about your look? Bring your make up bag and we will assess and make recommendations to update your look.</p>
    <p><span class="duration-label">DURATION:</span> Approx.1 hour to 1.30mins.</p>
    <div class="price-bar price-bar--makeup">Cost: $65.00</div>
    <div class="extras">
      Eyebrow shaping $25.00<br>
      Eyebrow Tint $15.00<br>
      Eyelash Tint $18.00<br>
      Eyelash extensions $25.00 (Reusable)
    </div>
  </section>
</div>
</body>
</html>
```